Cool modern, tech Business card design

Looking for a new business card design for our Managed IT Services company. We would like 2 sides, with the logo one one side horizontally and then the information on the back in either vertical or horizontal. We want our colors from the logo incorporated but also would like to see the color gray in there as well.

Target Market(s)

IT, Information Technology, Tech, Service

Industry/Entity Type

It Service

Contact Information for Business Card

Carl Penner
Managing Partner
(P)555-271-4830 ext xxx
(F)555-271-4831
www.brixtelcore.com

Font styles to use
Sans Serif

Colors
959595
000000
ec1f27

Requirements
Must have
• Logo on one side with some nice design or pattern
• Information on back in either vertical or horizontal format
Nice to have
• For it to look cool, tech, modern, stand out.

```html
<!DOCTYPE html>
<html lang="en">
<head>
<meta charset="utf-8">
<title>Brixtelcore business card</title>
<link href="https://fonts.googleapis.com/css2?family=Exo+2:wght@400;500;600&display=swap" rel="stylesheet">
<style>
  :root {
    --red: #ec1f27;
    --red-deep: #c8102e;
    --red-bright: #e8194a;
    --gray: #959595;
    --gray-light: #c9c9c9;
    --black: #000000;
    --white: #ffffff;
    --backdrop: #d4d4d4;
  }
  * { box-sizing: border-box; margin: 0; padding: 0; }
  html, body {
    width: 1200px; height: 800px; overflow: hidden;
    background: var(--backdrop);
    font-family: "Exo 2", Arial, sans-serif;
  }
  .stage {
    width: 1200px; height: 800px;
    display: flex; align-items: center; justify-content: center; gap: 50px;
  }
  .card {
    position: relative; width: 500px; height: 286px; overflow: hidden;
    box-shadow: 0 12px 28px rgba(0,0,0,.18);
  }

  /* Information side */
  .card-info { background: var(--white); }
  .info-top-bar { position: absolute; left: 0; top: 0; width: 230px; height: 12px; background: var(--red); }
  .info-side-bar { position: absolute; left: 0; top: 12px; width: 10px; height: 50px; background: var(--gray-light); }
  .brand {
    position: absolute; display: flex; align-items: center; gap: 7px;
    font-weight: 500; letter-spacing: .2px;
  }
  .card-info .brand { left: 34px; top: 44px; font-size: 26px; color: var(--red); }
  .brand-mark { width: 10px; height: 10px; background: currentColor; }
  .name-band {
    position: absolute; left: 262px; top: 112px; right: 0; height: 48px;
    background: var(--red); color: var(--white); padding: 5px 0 0 26px;
    border-top-left-radius: 14px;
  }
  .name-band::after {
    content: ""; position: absolute; left: 22px; bottom: -10px;
    border-left: 10px solid transparent; border-right: 10px solid transparent;
    border-top: 10px solid var(--red);
  }
  .person-name { font-size: 20px; font-weight: 500; line-height: 1.1; }
  .person-title { font-size: 10.5px; letter-spacing: .3px; }
  .contact-line {
    position: absolute; left: 244px; top: 160px; width: 2px; height: 80px; background: var(--red);
  }
  .contact-list { position: absolute; left: 231px; top: 170px; list-style: none; }
  .contact-item {
    display: flex; align-items: center; gap: 14px; height: 36px;
    color: var(--red); font-size: 14px; letter-spacing: .3px;
  }
  .contact-icon {
    width: 28px; height: 28px; border-radius: 50%; background: var(--white);
    border: 2px solid var(--red); display: flex; align-items: center; justify-content: center;
  }
  .contact-icon span {
    width: 20px; height: 20px; border-radius: 50%; background: var(--red);
    display: flex; align-items: center; justify-content: center;
  }

  /* Logo side */
  .card-logo { background: linear-gradient(150deg, var(--red-bright) 0%, var(--red) 50%, var(--red-deep) 100%); }
  .logo-glow {
    position: absolute; left: 120px; top: -40px; width: 200px; height: 160px; border-radius: 50%;
    background: radial-gradient(circle, rgba(255,80,120,.35), rgba(255,80,120,0) 70%);
  }
  .data-field {
    position: absolute; right: 40px; bottom: 36px; width: 230px; height: 80px;
    background: linear-gradient(180deg, rgba(255,60,110,.35), rgba(255,60,110,.05));
  }
  .card-logo .brand { right: 44px; top: 126px; font-size: 24px; color: var(--white); }
</style>
</head>
<body>
<main class="stage">
  <section class="card card-info" aria-label="Card information side">
    <div class="info-top-bar"></div>
    <div class="info-side-bar"></div>
    <div class="brand"><span class="brand-name">brixtelcore</span><span class="brand-mark"></span></div>

    <div class="name-band">
      <p class="person-name">Carl Penner</p>
      <p class="person-title">Managing Partner</p>
    </div>

    <div class="contact-line"></div>
    <ul class="contact-list">
      <li class="contact-item">
        <span class="contact-icon"><span>
          <svg width="12" height="12" viewBox="0 0 24 24"><path fill="#fff" d="M6.6 10.8a15 15 0 0 0 6.6 6.6l2.2-2.2a1 1 0 0 1 1-.25 11.4 11.4 0 0 0 3.6.57 1 1 0 0 1 1 1V20a1 1 0 0 1-1 1A17 17 0 0 1 3 4a1 1 0 0 1 1-1h3.5a1 1 0 0 1 1 1c0 1.25.2 2.45.57 3.57a1 1 0 0 1-.25 1z"/></svg>
        </span></span>
        <span class="contact-text">555-271-4830</span>
      </li>
      <li class="contact-item">
        <span class="contact-icon"><span>
          <svg width="12" height="12" viewBox="0 0 24 24"><rect x="5" y="3" width="14" height="6" fill="#fff"/><rect x="3" y="10" width="18" height="9" rx="1" fill="#fff"/><rect x="7" y="14" width="10" height="7" fill="#fff" stroke="#ec1f27" stroke-width="1.5"/></svg>
        </span></span>
        <span class="contact-text">555-271-4831</span>
      </li>
      <li class="contact-item">
        <span class="contact-icon"><span>
          <svg width="12" height="12" viewBox="0 0 24 24" fill="none" stroke="#fff" stroke-width="2"><circle cx="12" cy="12" r="9"/><path d="M3 12h18M12 3c3 3 3 15 0 18M12 3c-3 3-3 15 0 18"/></svg>
        </span></span>
        <span class="contact-text">www.brixtelcore.com</span>
      </li>
    </ul>
  </section>

  <section class="card card-logo" aria-label="Card logo side">
    <div class="logo-glow" role="img" aria-label="Soft light decoration area"></div>
    <div class="data-field" role="img" aria-label="Decorative data bar pattern area"></div>
    <div class="brand"><span class="brand-name">brixtelcore</span><span class="brand-mark"></span></div>
  </section>
</main>
</body>
</html>
```